Quillo Business Card Design

Looking for elegant and super stylish business cards. Enclosed is the card design we are using now. We need something more contemporary.

Target Market(s)

We are a catering company focusing on weddings and corporate events.

Industry/Entity Type

Caterer

Contact Information for Business Card

Please use similar font to our current cards

Colors
0592cd

Requirements
Must have
• Color and be very unique. Also, please use logo (with or without the castle.)

```html
<!DOCTYPE html>
<html lang="en">
<head>
<meta charset="utf-8">
<title>Quillo Catering – Business Card</title>
<link rel="stylesheet" href="https://fonts.googleapis.com/css2?family=Philosopher:wght@400;700&display=swap">
<style>
  :root {
    --card-bg: #313034;
    --text-light: #ffffff;
    --brand-blue: #0592cd;
    --text-soft: #d9dde0;
  }
  html, body {
    margin: 0;
    padding: 0;
    width: 1200px;
    height: 720px;
    overflow: hidden;
    background: var(--card-bg);
  }
  .card {
    position: relative;
    width: 1200px;
    height: 720px;
    overflow: hidden;
    background: var(--card-bg);
    font-family: "Philosopher", sans-serif;
    color: var(--text-light);
  }
  .holder-name {
    position: absolute;
    left: 82px;
    top: 70px;
    margin: 0;
    font-size: 56px;
    font-weight: 400;
    line-height: 1;
  }
  .holder-name .surname { color: var(--brand-blue); }
  .holder-title {
    position: absolute;
    left: 81px;
    top: 138px;
    margin: 0;
    font-size: 31px;
    font-weight: 400;
    letter-spacing: 0.36em;
    line-height: 1;
    white-space: nowrap;
  }
  .brand {
    position: absolute;
    right: 84px;
    top: 140px;
    display: flex;
    align-items: center;
    gap: 18px;
    color: var(--brand-blue);
    font-size: 78px;
    font-weight: 400;
    line-height: 1;
  }
  .brand-square {
    width: 26px;
    height: 26px;
    background: var(--brand-blue);
  }
  .contact {
    position: absolute;
    left: 83px;
    top: 390px;
    margin: 0;
    font-style: normal;
    font-size: 32px;
    line-height: 42px;
    color: var(--text-soft);
  }
  .contact p { margin: 0; }
  .contact .address { margin-bottom: 8px; color: var(--text-light); }
  .contact .lines p { line-height: 40px; }
  .contact .label { color: var(--brand-blue); }
</style>
</head>
<body>
  <main class="card">
    <h1 class="holder-name">Selim <span class="surname">Haddad</span></h1>
    <p class="holder-title">Chief Executive Officer</p>

    <div class="brand" aria-label="Quillo Catering">
      <span class="brand-square"></span>
      <span class="brand-name">Quillo</span>
    </div>

    <address class="contact">
      <div class="address">
        <p>4318 Marlow Street</p>
        <p>Harbor Point, California 90412</p>
      </div>
      <div class="lines">
        <p class="office"><span class="label">Office:</span> 555 310 4826 ext. 204</p>
        <p class="fax"><span class="label">Fax:</span> 555 742 1930</p>
        <p class="email">s@thequillocatering.com</p>
        <p class="web">www.thequillocatering.com</p>
      </div>
    </address>
  </main>
</body>
</html>
```